Business Card Design

Company name is: Tallowmere Rescue Skills, LLC. We teach CPR/AED, First Aid, Bloodborne Pathogens and other health and safety classes. Looking for an eye-catching, progressive, cutting edge design.

Industry/Entity Type

Health

Contact Information for Business Card

Dale Fenwarick (555.218.4703)
Nora Quillstead (555.276.9148)
email is info@tallowmererescue.example
website is www.TallowmereRescue.example

```html
<!DOCTYPE html>
<html lang="en">
<head>
<meta charset="UTF-8">
<title>Tallowmere Rescue Skills, LLC — Business Card</title>
<link rel="stylesheet" href="https://fonts.googleapis.com/css2?family=Jost:ital,wght@0,400;0,500;1,700&display=swap">
<style>
  :root {
    --card-bg: #ffffff;
    --navy: #2a2f86;
    --ink: #111111;
    --rule: #8fc3e8;
    --tile-light: #cdeefc;
    --tile-mid: #4fa8ec;
    --tile-deep: #233f9c;
  }
  * { margin: 0; padding: 0; box-sizing: border-box; }
  html, body {
    width: 1200px;
    height: 705px;
    overflow: hidden;
    background: var(--card-bg);
  }
  .card {
    position: relative;
    width: 1200px;
    height: 705px;
    background: var(--card-bg);
    font-family: "Jost", "Helvetica Neue", Arial, sans-serif;
    overflow: hidden;
  }
  .mosaic-field {
    position: absolute;
    inset: 0;
    width: 1200px;
    height: 705px;
  }
  .company {
    position: absolute;
    left: 60px;
    top: 88px;
    width: 600px;
    padding: 18px 0 16px;
    border-top: 2px solid var(--rule);
    border-bottom: 2px solid var(--rule);
  }
  .company-name {
    font-size: 37px;
    font-weight: 400;
    letter-spacing: 0.5px;
    text-transform: uppercase;
    color: var(--navy);
    line-height: 1;
    white-space: nowrap;
  }
  .contact-person {
    position: absolute;
    left: 60px;
  }
  .person-name {
    font-size: 30px;
    font-weight: 400;
    color: var(--navy);
    line-height: 1.25;
  }
  .person-phone {
    font-size: 30px;
    font-weight: 500;
    color: var(--ink);
    line-height: 1.25;
  }
  .person-one { top: 200px; }
  .person-two { top: 312px; }
  .contact-line {
    position: absolute;
    left: 60px;
    font-size: 29px;
    color: var(--ink);
    line-height: 1.2;
  }
  .contact-line .label { color: var(--navy); }
  .email-line { top: 434px; }
  .web-line { top: 487px; }
  .services {
    position: absolute;
    left: 60px;
    top: 580px;
    font-size: 24px;
    font-weight: 700;
    font-style: italic;
    letter-spacing: 0.3px;
    text-transform: uppercase;
    color: var(--navy);
    white-space: nowrap;
  }
</style>
</head>
<body>
  <div class="card">
    <svg class="mosaic-field" viewBox="0 0 1200 705" role="img" aria-label="Decorative blue geometric triangle mosaic along the right edge">
      <defs>
        <linearGradient id="mosaic-fill" x1="0" y1="0" x2="1" y2="0.3">
          <stop offset="0" stop-color="var(--tile-light)"/>
          <stop offset="0.45" stop-color="var(--tile-mid)"/>
          <stop offset="1" stop-color="var(--tile-deep)"/>
        </linearGradient>
      </defs>
      <polygon fill="url(#mosaic-fill)"
        points="860,0 1200,0 1200,705 880,705 820,560 860,420 800,300 840,150"/>
    </svg>

    <div class="company">
      <h1 class="company-name">Tallowmere Rescue Skills, LLC.</h1>
    </div>

    <div class="contact-person person-one">
      <p class="person-name">Dale Fenwarick</p>
      <p class="person-phone">555.218.4703</p>
    </div>

    <div class="contact-person person-two">
      <p class="person-name">Nora Quillstead</p>
      <p class="person-phone">555.276.9148</p>
    </div>

    <p class="contact-line email-line"><span class="label">Email:</span> info@tallowmererescue.example</p>
    <p class="contact-line web-line"><span class="label">Web:</span> www.TallowmereRescue.example</p>

    <p class="services">CPR/AED, First Aid &amp; Bloodborne Pathegon Training</p>
  </div>
</body>
</html>
```